Silverbrook Community Wellness Exchange Seeks E-Newsletter Design

We need an electronic newsletter design for regular communication from our organization. We require an editable Mailchimp template that must be optimized for use on mobile phones. For more information about creating a usable and editable HTML Mailchimp template, please read this guide: https://quorvanlinks.net/kp7Wzt

The primary audiences for the electronic newsletter are professionals in healthy aging, public health, and brain health. Many of the recipients will be American Indian or Alaska Natives or professionals who provide public health services to American Indian or Alaska Native people.

The e-newsletter design should complement the colors of the Clearwater Pathways Program project logo. The project logo and color scheme are attached to this design brief. The logo should be at the top of the page.

Attributes that we’d like to come to mind when people our electronic newsletter and think about our organization: professional, informed, trustworthy, respected, innovative, hopeful, positive, welcoming.

We intend to have a combination of written content, videos, and photos. We also will link to outside content.

The e-newsletter will have the following editable sections:
1. Silverbrook Community Wellness Exchange Updates: The purpose of the program updates section is for the organization to feature all of the good work accomplished over the month and to highlight why the organization is a leader in aging and brain health.
2. Community Updates: The purpose of the blog section is to promote approaches, programs, policies, funding, relationships, etc. that advance the Clearwater Pathways Program’s mission and align with the values of organization. This section should make people feel informed, hopeful, and positive. This section will feature photos and should have the ability to feature a video.
3. Advisory Group Feature: The purpose of the Advisory Group Feature section is to highlight the contributions and wealth of experience of our Advisory Group members. This section will feature a photo.
4. Promising Practices: The purpose of the Promising Practices section is to share examples of programs/initiatives/policies that align with the values and mission of the Clearwater Pathways Program. This section should make people feel informed, hopeful, and positive. This section will also feature
5. Featured Resources: The purpose of the featured resources section is to share resources, upcoming events and opportunities for readers to engage in content that further advances the Clearwater Pathways Program’s mission. This section will include several links to outside content.
6. Where You Can Find Us: The purpose of the “Where You Can Find Us” section is to share the organization’s contact information and additional ways to engage with the organization and related content. This needs to include links to social media platforms and our website.

Target Market(s)

Font styles to use
Sans Serif

Requirements
Must have
• We require an editable Mailchimp template that is optimized for use on mobile phones. For more information about creating a usable and editable HTML Mailchimp template, please read this guide: https://quorvanlinks.net/kp7Wzt
Should not have
• feathers

```html
<!DOCTYPE html>
<html lang="en">
<head>
<meta charset="utf-8">
<title>Silverbrook Community Wellness Exchange – Newsletter</title>
<link href="https://fonts.googleapis.com/css2?family=Bebas+Neue&family=Montserrat:wght@600&family=Rubik:wght@500&family=PT+Sans:wght@400;700&display=swap" rel="stylesheet">
<style>
  :root {
    --teal: #4fa9b4;
    --teal-light: #6fd0de;
    --rust: #b0564a;
    --header-top: #4ea9b3;
    --header-mid: #8d8f9f;
    --header-bottom: #b05a4c;
    --ink: #2b2b2b;
    --rule: #d8d8d8;
    --disc: #f6f6f6;
    --disc-edge: #e4e4e4;
    --footer: #6b6b6b;
    --page: #ffffff;
    --white: #ffffff;
  }
  * { box-sizing: border-box; margin: 0; padding: 0; }
  html, body { width: 900px; height: 1200px; overflow: hidden; background: var(--page); }
  .newsletter {
    position: absolute; left: 224px; top: 174px;
    width: 452px; height: 851px;
    background: var(--white);
    box-shadow: 0 0 3px rgba(0,0,0,0.2);
    overflow: hidden;
  }
  .masthead {
    position: absolute; left: 0; top: 0; width: 452px; height: 231px;
    background: linear-gradient(180deg, var(--header-top) 0%, var(--header-mid) 55%, var(--header-bottom) 100%);
  }
  .brand { position: absolute; display: flex; align-items: center; gap: 9px; }
  .brand-mark { border-radius: 50%; border: 2px solid var(--white); flex: none; }
  .brand-name {
    font-family: "Montserrat", sans-serif; font-weight: 600; color: var(--white);
    text-transform: uppercase; line-height: 1.12;
  }
  .masthead .brand { left: 30px; top: 31px; }
  .masthead .brand-mark { width: 56px; height: 56px; }
  .masthead .brand-name { font-size: 11px; width: 150px; }
  .hero-art {
    position: absolute; left: 208px; top: 66px; width: 244px; height: 138px;
    background: radial-gradient(ellipse at 58% 48%, rgba(140,210,240,0.9) 0%, rgba(110,170,220,0.55) 40%, rgba(140,150,180,0) 72%);
  }
  .hero-title {
    position: absolute; left: 28px; top: 117px;
    font-family: "Bebas Neue", sans-serif; font-weight: 400; font-size: 37px; line-height: 33px;
    color: var(--white); letter-spacing: 0.3px;
  }
  .hero-subtitle {
    position: absolute; left: 27px; top: 184px;
    font-family: "Montserrat", sans-serif; font-weight: 600; font-size: 12px;
    color: var(--teal-light); letter-spacing: 0.2px;
  }
  .section { position: absolute; width: 156px; text-align: center; }
  .section-icon { display: block; margin: 0 auto; width: 96px; height: 60px; }
  .section-title {
    font-family: "Rubik", sans-serif; font-weight: 500; font-size: 8px;
    color: var(--rust); line-height: 10px; margin-top: 15px;
  }
  .section-text {
    font-family: "PT Sans", sans-serif; font-size: 6.2px; line-height: 8.2px;
    color: var(--ink); margin-top: 5px;
  }
  .col-left { left: 43px; }
  .col-right { left: 256px; }
  .row-1 { top: 259px; }
  .row-2 { top: 445px; }
  .row-3 { top: 624px; }
  .glyph { fill: none; stroke: var(--rust); stroke-width: 1.4; stroke-linecap: round; stroke-linejoin: round; }
  .footer {
    position: absolute; left: 0; top: 782px; width: 452px; height: 69px;
    background: var(--footer);
  }
  .footer .brand { left: 30px; top: 16px; gap: 7px; }
  .footer .brand-mark { width: 36px; height: 36px; }
  .footer .brand-name { font-size: 8px; width: 100px; }
  .site-link {
    position: absolute; left: 267px; top: 25px; width: 157px; height: 21px;
    border-radius: 11px; background: var(--teal); text-align: center;
    font-family: "PT Sans", sans-serif; font-weight: 700; font-size: 10px; line-height: 21px; color: var(--white);
  }
</style>
</head>
<body>
<main class="newsletter">
  <header class="masthead">
    <div class="brand">
      <span class="brand-mark"></span>
      <span class="brand-name">Silverbrook Community<br>Wellness Exchange</span>
    </div>
    <div class="hero-art" role="img" aria-label="Glowing digital brain illustration with network lines"></div>
    <h1 class="hero-title">SILVERBROOK<br>COMMUNITY</h1>
    <p class="hero-subtitle">WELLNESS EXCHANGE</p>
  </header>

  <section class="section col-left row-1">
    <svg class="section-icon" viewBox="0 0 96 60">
      <line x1="0" y1="34" x2="96" y2="34" stroke="var(--rule)" stroke-width="1.5"/>
      <path d="M17 34 A31 31 0 0 1 79 34" fill="none" stroke="var(--teal)" stroke-width="2.2"/>
      <circle cx="48" cy="33" r="27" fill="var(--disc)" stroke="var(--disc-edge)"/>
      <g class="glyph">
        <rect x="39" y="21" width="18" height="23" rx="1.5"/>
        <line x1="43" y1="27" x2="53" y2="27"/>
        <line x1="43" y1="31" x2="53" y2="31"/>
        <line x1="43" y1="35" x2="53" y2="35"/>
        <line x1="43" y1="39" x2="49" y2="39"/>
      </g>
    </svg>
    <h2 class="section-title">Silverbrook Community Wellness<br>Exchange Updates</h2>
    <p class="section-text">The purpose of the program updates section is for the organization to feature all of the good work accomplished over the month and to highlight why the organization is a leader in aging and brain health.</p>
  </section>

  <section class="section col-right row-1">
    <svg class="section-icon" viewBox="0 0 96 60">
      <line x1="0" y1="34" x2="96" y2="34" stroke="var(--rule)" stroke-width="1.5"/>
      <path d="M17 34 A31 31 0 0 1 79 34" fill="none" stroke="var(--teal)" stroke-width="2.2"/>
      <circle cx="48" cy="33" r="27" fill="var(--disc)" stroke="var(--disc-edge)"/>
      <g class="glyph">
        <path d="M36 22 h16 a2 2 0 0 1 2 2 v9 a2 2 0 0 1 -2 2 h-9 l-4 4 v-4 h-3 a2 2 0 0 1 -2 -2 v-9 a2 2 0 0 1 2 -2 z"/>
        <path d="M56 29 h4 a2 2 0 0 1 2 2 v8 a2 2 0 0 1 -2 2 h-2 v4 l-4 -4 h-6 a2 2 0 0 1 -2 -2 v-2"/>
      </g>
    </svg>
    <h2 class="section-title">Community Updates</h2>
    <p class="section-text">The purpose of the blog section is to promote approaches, programs, policies, funding, relationships, etc. that advance the Clearwater Pathways Program’s mission and align with the values of organization. This section should make people feel informed, hopeful, and positive. This section will feature photos and should have the ability to feature a video.</p>
  </section>

  <section class="section col-left row-2">
    <svg class="section-icon" viewBox="0 0 96 60">
      <line x1="0" y1="34" x2="96" y2="34" stroke="var(--rule)" stroke-width="1.5"/>
      <path d="M17 34 A31 31 0 0 1 79 34" fill="none" stroke="var(--teal)" stroke-width="2.2"/>
      <circle cx="48" cy="33" r="27" fill="var(--disc)" stroke="var(--disc-edge)"/>
      <g class="glyph">
        <path d="M48 20 l3.6 7.4 8.1 1.2 -5.9 5.7 1.4 8.1 -7.2 -3.8 -7.2 3.8 1.4 -8.1 -5.9 -5.7 8.1 -1.2 z"/>
      </g>
    </svg>
    <h2 class="section-title">Advisory Group Feature</h2>
    <p class="section-text">The purpose of the Advisory Group Feature section is to highlight the contributions and wealth of experience of our Advisory Group members. This section will feature a photo.</p>
  </section>

  <section class="section col-right row-2">
    <svg class="section-icon" viewBox="0 0 96 60">
      <line x1="0" y1="34" x2="96" y2="34" stroke="var(--rule)" stroke-width="1.5"/>
      <path d="M17 34 A31 31 0 0 1 79 34" fill="none" stroke="var(--teal)" stroke-width="2.2"/>
      <circle cx="48" cy="33" r="27" fill="var(--disc)" stroke="var(--disc-edge)"/>
      <g class="glyph">
        <path d="M48 44 C40 38 35 33 35 27.5 a6 6 0 0 1 13 -2.5 a6 6 0 0 1 13 2.5 C61 33 56 38 48 44 z"/>
      </g>
    </svg>
    <h2 class="section-title">Promising Practices</h2>
    <p class="section-text">The purpose of the Promising Practices section is to share examples of programs/initiatives/policies that align with the values and mission of the Clearwater Pathways Program. This section should make people feel informed, hopeful, and positive. This section will also feature</p>
  </section>

  <section class="section col-left row-3">
    <svg class="section-icon" viewBox="0 0 96 60">
      <line x1="0" y1="34" x2="96" y2="34" stroke="var(--rule)" stroke-width="1.5"/>
      <path d="M17 34 A31 31 0 0 1 79 34" fill="none" stroke="var(--teal)" stroke-width="2.2"/>
      <circle cx="48" cy="33" r="27" fill="var(--disc)" stroke="var(--disc-edge)"/>
      <circle cx="48" cy="33" r="9" fill="none" stroke="var(--rust)" stroke-width="3.5" stroke-dasharray="3.5 3.57"/>
      <g class="glyph">
        <circle cx="48" cy="33" r="6.5"/>
        <circle cx="48" cy="33" r="2.5"/>
      </g>
    </svg>
    <h2 class="section-title">Featured Resources</h2>
    <p class="section-text">The purpose of the featured resources section is to share resources, upcoming events and opportunities for readers to engage in content that further advances the Clearwater Pathways Program’s mission. This section will include several links to outside content.</p>
  </section>

  <section class="section col-right row-3">
    <svg class="section-icon" viewBox="0 0 96 60">
      <line x1="0" y1="34" x2="96" y2="34" stroke="var(--rule)" stroke-width="1.5"/>
      <path d="M17 34 A31 31 0 0 1 79 34" fill="none" stroke="var(--teal)" stroke-width="2.2"/>
      <circle cx="48" cy="33" r="27" fill="var(--disc)" stroke="var(--disc-edge)"/>
      <circle cx="44" cy="29" r="7.5" fill="none" stroke="var(--rust)" stroke-width="1.6"/>
      <line x1="49.5" y1="34.5" x2="58" y2="43" stroke="var(--rust)" stroke-width="3" stroke-linecap="round"/>
    </svg>
    <h2 class="section-title">Where You Can Find Us</h2>
    <p class="section-text">The purpose of the “Where You Can Find Us” section is to share the organization’s contact information and additional ways to engage with the organization and related content. This needs to include links to social media platforms and our website.</p>
  </section>

  <footer class="footer">
    <div class="brand">
      <span class="brand-mark"></span>
      <span class="brand-name">Silverbrook Community<br>Wellness Exchange</span>
    </div>
    <span class="site-link">www.silverbrookwellness.org</span>
  </footer>
</main>
</body>
</html>
```